Garden Design Business Card Design

A business card design for garden design company called ;
ROOTED IN CLAY which has a great deal of maintenance but
wishes to promote its expertise for design in planting and garden
design, but in an informal manner.

Would love to see quite a rustic approach,very strong and innovative and taking risks on typography. Am open to ideas with
colours,as memorability is important.

Target Market(s)

General public 40/50 years in a very trendy area

Industry/Entity Type

Business

Contact Information for Business Card

ROOTED IN CLAY. Garden design and maintenance.
Peter Holcombe
Telephone 01632 960417 Mobile 07700 900382

```html
<!DOCTYPE html>
<html lang="en">
<head>
<meta charset="utf-8">
<title>Rooted in Clay – Business Card</title>
<link rel="stylesheet" href="https://fonts.googleapis.com/css2?family=Lato:wght@400&display=swap">
<style>
  :root {
    --sky-top: #5ee3ec;
    --sky-bottom: #8fe4df;
    --grass-top: #aaf23a;
    --grass-bottom: #64ba00;
    --text-light: #effbfb;
    --sprout-fill: #c8ecb4;
    --sprout-edge: #9fd04a;
  }
  html, body {
    margin: 0;
    padding: 0;
    width: 1200px;
    height: 791px;
    overflow: hidden;
  }
  .card {
    position: relative;
    width: 1200px;
    height: 791px;
    overflow: hidden;
    font-family: "Lato", "Gill Sans", sans-serif;
    color: var(--text-light);
    background: linear-gradient(to bottom, var(--sky-top) 0%, var(--sky-bottom) 60%);
  }
  .grass-band {
    position: absolute;
    left: 0;
    top: 477px;
    width: 1200px;
    height: 314px;
    background: linear-gradient(to bottom, var(--grass-top) 0%, var(--grass-bottom) 100%);
  }
  .line {
    position: absolute;
    margin: 0;
    line-height: 1;
    white-space: nowrap;
    font-weight: 400;
  }
  .brand-name {
    left: 0;
    width: 1200px;
    top: 88px;
    text-align: center;
    font-size: 112px;
    letter-spacing: 4px;
  }
  .tagline {
    left: 0;
    width: 1190px;
    top: 212px;
    text-align: center;
    font-size: 50px;
    letter-spacing: 2px;
  }
  .contact-name {
    left: 0;
    width: 1176px;
    top: 503px;
    text-align: center;
    font-size: 60px;
  }
  .phone {
    right: 253px;
    top: 592px;
    font-size: 58px;
    text-align: right;
  }
  .mobile {
    right: 253px;
    top: 652px;
    font-size: 58px;
    text-align: right;
  }
  .sprout-row {
    position: absolute;
    left: 0;
    top: 318px;
    width: 1200px;
    height: 160px;
  }
</style>
</head>
<body>
  <div class="card">
    <div class="grass-band"></div>

    <svg class="sprout-row" width="1200" height="160" viewBox="0 0 1200 160">
      <rect role="img" aria-label="Sprout illustration" x="88" y="0" width="90" height="159" rx="30" fill="var(--sprout-fill)" stroke="var(--sprout-edge)" stroke-width="2" opacity="0.55"/>
      <rect role="img" aria-label="Sprout illustration" x="313" y="0" width="90" height="159" rx="30" fill="var(--sprout-fill)" stroke="var(--sprout-edge)" stroke-width="2" opacity="0.55"/>
      <rect role="img" aria-label="Sprout illustration" x="550" y="0" width="90" height="159" rx="30" fill="var(--sprout-fill)" stroke="var(--sprout-edge)" stroke-width="2" opacity="0.55"/>
      <rect role="img" aria-label="Sprout illustration" x="798" y="0" width="90" height="159" rx="30" fill="var(--sprout-fill)" stroke="var(--sprout-edge)" stroke-width="2" opacity="0.55"/>
      <rect role="img" aria-label="Sprout illustration" x="1023" y="0" width="90" height="159" rx="30" fill="var(--sprout-fill)" stroke="var(--sprout-edge)" stroke-width="2" opacity="0.55"/>
    </svg>

    <h1 class="line brand-name">ROOTED IN CLAY</h1>
    <p class="line tagline">GARDEN DESIGN AND MAINTENANCE</p>

    <p class="line contact-name">PETER HOLCOMBE</p>
    <p class="line phone">TELEPHONE 01632 960417</p>
    <p class="line mobile">MOBILE 07700 900382</p>
  </div>
</body>
</html>
```